Plakat-Design zum Thema Personalabteilung
sehr zufrieden, Änderungen wurden schnell umgesetzt und Kommunikation war sehr gut
Zielgruppe
Morvena Software hat sich zum Ziel gesetzt, kleinen und mittleren Unternehmen über das Web schnell einsetzbare Lösungen zur Verfügung zu stellen, die ohne große Projektkosten direkt von der Personalabteilung genutzt werden können.
Frauen mittleren Alters in der Personalabteilung.
Aufgabenstellung
Formatvorgaben siehe Dokument 'Druckdatenblatt_Grossplakat'.
Wie haben uns 2 Designvorschläge überlegt. Bitte wählen Sie mindestens einen Vorschlag oder machen Sie zu jedem Design einen Entwurf.
Vorschlag 1:
Variante 1:
Dicker ekliger Chef
Sprechblase 1: meine Tussi in der Personalabteilung arbeitet 24/7 für mich
Sprechblase 2: und das völlig kostenfrei
stabwerkel.net
Footer mit: Luxemburg – Frankfurt – Leipzig/Halle – Wien
Variante 2:
Headline: Neues aus der Personalabteilung
Sprechblase 1: meine Tussi arbeitet 24/7 für mich
Vorschlag 2:
Tussi (Avatar)
Sprechblase: Ich arbeite 24/7 für meinen Chef, völlig kostenfrei und ich liebe es
kanzleigrund.cloud

```html
<!DOCTYPE html>
<html lang="de">
<head>
<meta charset="utf-8">
<title>Neues aus der Personalabteilung – Großplakat</title>
<link href="https://fonts.googleapis.com/css2?family=Bangers&family=Patrick+Hand&family=Gochi+Hand&display=swap" rel="stylesheet">
<style>
  :root {
    --yellow: #ffec00;
    --ink: #111111;
    --pink: #e3178c;
    --green: #5db432;
    --page: #ffffff;
    --photo-light: #b9b9b9;
    --photo-dark: #3a3a3a;
    --boss-dark: #1e1e1e;
    --boss-mid: #4a4a4a;
  }
  html, body {
    margin: 0;
    padding: 0;
    width: 1200px;
    height: 982px;
    overflow: hidden;
    background: var(--page);
  }
  .poster {
    position: absolute;
    left: 0;
    top: 74px;
    width: 1200px;
    height: 834px;
    overflow: hidden;
  }
  .poster__backdrop {
    position: absolute;
    left: 0;
    top: 101px;
    width: 1200px;
    height: 733px;
    background: radial-gradient(ellipse at 60% 30%, var(--photo-light), #8e8e8e 55%, var(--photo-dark) 100%);
  }
  .poster__boss-photo {
    position: absolute;
    left: 190px;
    top: 112px;
    width: 740px;
    height: 722px;
    border-radius: 46% 46% 0 0 / 38% 38% 0 0;
    background: linear-gradient(180deg, var(--boss-mid) 0%, #333333 45%, var(--boss-dark) 100%);
    box-shadow: 0 0 60px 20px rgba(30,30,30,0.35);
  }
  .poster__header {
    position: absolute;
    left: 0;
    top: 0;
    width: 1200px;
    height: 101px;
    background: var(--yellow);
    display: flex;
    align-items: center;
    justify-content: center;
  }
  .headline {
    margin: 8px 0 0;
    font-family: "Bangers", cursive;
    font-weight: 400;
    font-size: 64px;
    letter-spacing: 2px;
    color: var(--ink);
    transform: skewX(-6deg);
  }
  .bubble {
    position: absolute;
  }
  .bubble svg {
    position: absolute;
    inset: 0;
    width: 100%;
    height: 100%;
    overflow: visible;
  }
  .bubble__text {
    position: absolute;
    margin: 0;
    font-family: "Gochi Hand", cursive;
    color: #ffffff;
    text-transform: uppercase;
    text-align: center;
    line-height: 1.12;
    white-space: nowrap;
  }
  .bubble--boss {
    left: 78px;
    top: 138px;
    width: 352px;
    height: 222px;
  }
  .bubble--boss .bubble__text {
    left: 26px;
    top: 36px;
    width: 300px;
    font-size: 24px;
    transform: rotate(-7deg);
  }
  .bubble--free {
    left: 786px;
    top: 244px;
    width: 224px;
    height: 150px;
  }
  .bubble--free .bubble__text {
    left: 14px;
    top: 20px;
    width: 196px;
    font-size: 26px;
    transform: rotate(6deg);
  }
  .locations {
    position: absolute;
    left: 860px;
    top: 702px;
    width: 320px;
    margin: 0;
    font-family: "Patrick Hand", cursive;
    font-size: 28px;
    line-height: 1.3;
    color: var(--ink);
    text-align: center;
  }
  .poster__footer {
    position: absolute;
    left: 390px;
    top: 744px;
    width: 425px;
    height: 90px;
    background: var(--yellow);
    display: flex;
    align-items: center;
    justify-content: center;
  }
  .web-address {
    margin: 0;
    font-family: "Bangers", cursive;
    font-size: 46px;
    letter-spacing: 2px;
    color: var(--ink);
    transform: skewX(-6deg);
  }
</style>
</head>
<body>
  <main class="poster">
    <div class="poster__backdrop" role="img" aria-label="Grauer Hintergrund mit Zigarrenrauch"></div>
    <div class="poster__boss-photo" role="img" aria-label="Foto: Chef mit Sonnenbrille und Zigarre im dunklen Anzug, zeigt mit dem Daumen auf den Betrachter"></div>

    <header class="poster__header">
      <h1 class="headline">NEUES AUS DER PERSONALABTEILUNG</h1>
    </header>

    <div class="bubble bubble--boss">
      <svg viewBox="0 0 352 222" aria-hidden="true">
        <path d="M176 8 C280 4 348 40 344 96 C340 150 270 180 190 182 L168 214 L160 184 C80 184 8 160 8 104 C8 48 80 12 176 8 Z"
              fill="var(--pink)" stroke="var(--ink)" stroke-width="3"/>
        <path d="M300 30 C330 44 346 70 338 104" fill="none" stroke="var(--ink)" stroke-width="2"/>
        <path d="M40 170 C70 186 110 194 150 194" fill="none" stroke="var(--ink)" stroke-width="2"/>
      </svg>
      <p class="bubble__text">Meine Tussi in<br>der Personalabteilung<br>arbeitet 24/7<br>für mich!</p>
    </div>

    <div class="bubble bubble--free">
      <svg viewBox="0 0 224 150" aria-hidden="true">
        <path d="M18 6 L214 14 C220 14 222 18 222 24 L214 118 C214 124 210 126 204 126 L50 124 L28 146 L32 122 L12 120 C6 120 4 116 4 110 L10 14 C10 8 12 6 18 6 Z"
              fill="var(--green)" stroke="var(--ink)" stroke-width="3"/>
        <path d="M14 2 L212 10" fill="none" stroke="var(--ink)" stroke-width="1.5"/>
      </svg>
      <p class="bubble__text">Und das<br>völlig<br>kostenfrei!</p>
    </div>

    <p class="locations">Luxemburg - Frankfurt<br>Leipzig/Halle - Wien</p>

    <footer class="poster__footer">
      <p class="web-address">STABWERKEL.NET</p>
    </footer>
  </main>
</body>
</html>
```